Bref créative
Need stationery for my new logo
stationery, business cards, letterheads, welcome postcards, email signature,envelopes,fax header etc
Bright & Fun-filled
Mathis Dorvelle
Responsable commercial
Rue des Vignots Hauts 42B
B-4280 CORNIVAL
Belgique
mathis@nexo-vault.be
www.nexo-vault.be
Can be mainly the logo, or few words describing our activity like :
Gestion infrastructure informatique, servers, postes de travail email domaine windows réseau sécurité antivirus antispam emails hosting cloud

```html
<!DOCTYPE html>
<html lang="fr">
<head>
<meta charset="utf-8">
<title>Nexo-Vault — papeterie</title>
<link href="https://fonts.googleapis.com/css2?family=Open+Sans:wght@400;600;800&display=swap" rel="stylesheet">
<style>
  :root{
    --bg-light:#9a9a9a;
    --bg-dark:#6e6e6e;
    --paper:#ffffff;
    --red:#c6281c;
    --red-dark:#8e1a10;
    --grey:#8c8c8c;
    --ink:#3b3b3b;
    --soft:#f0eeee;
  }
  *{margin:0;padding:0;box-sizing:border-box}
  html,body{width:1200px;height:626px;overflow:hidden}
  body{
    background:radial-gradient(ellipse at 50% 45%,var(--bg-light) 0%,var(--bg-dark) 100%);
    font-family:"Open Sans",Arial,sans-serif;
    color:var(--ink);
    position:relative;
  }
  .piece{position:absolute;background:var(--paper);overflow:hidden;box-shadow:0 2px 6px rgba(0,0,0,.35)}
  .piece svg.wave{position:absolute;left:0;bottom:0;width:100%}
  .brand{display:flex;align-items:center;gap:6px}
  .brand-dot{width:14px;height:14px;border-radius:50%;background:var(--red);flex:none}
  .brand-name{font-weight:800;color:var(--ink);letter-spacing:.5px;line-height:1}
  .brand-url{font-size:7px;font-weight:600;color:var(--ink);margin-left:20px;margin-top:2px;letter-spacing:.6px}
  .small{font-size:4.6px;line-height:1.45;color:var(--ink)}

  /* business cards */
  .card-front{left:29px;top:259px;width:187px;height:106px}
  .card-front .small{position:absolute;right:12px;top:10px;text-align:right}
  .card-front .brand-block{position:absolute;left:36px;top:40px}
  .card-front .brand-name{font-size:16px}
  .card-front .brand-dot{width:11px;height:11px}
  .card-front .brand-url{font-size:6px;margin-left:17px}
  .card-back{left:29px;top:379px;width:187px;height:101px}
  .card-back .small{position:absolute;left:0;right:0;top:14px;text-align:center}

  /* letterhead */
  .letterhead{left:233px;top:29px;width:384px;height:588px}
  .letterhead .brand-block{position:absolute;left:20px;top:30px}
  .letterhead .brand-name{font-size:22px}
  .letterhead .brand-url{font-size:8px;margin-left:22px}
  .letterhead .contact{position:absolute;left:268px;top:18px}
  .letterhead .faint-mark{
    position:absolute;left:0;right:0;top:230px;text-align:center;
    font-weight:800;font-size:44px;color:var(--soft);letter-spacing:2px
  }

  /* envelopes */
  .envelope-back{left:677px;top:89px;width:492px;height:218px;background:var(--red)}
  .envelope-back svg{position:absolute;inset:0;width:100%;height:100%}
  .envelope-front{left:677px;top:336px;width:492px;height:209px}
  .envelope-front .brand-block{position:absolute;left:26px;top:66px}
  .envelope-front .brand-name{font-size:22px}
  .envelope-front .brand-url{font-size:8px;margin-left:22px}
  .envelope-front .contact{position:absolute;left:372px;top:60px}
</style>
</head>
<body>

<section class="piece card-front">
  <p class="small">Mathis Dorvelle<br>Responsable commercial<br>mathis@nexo-vault.be<br>T. +32 4 512 00 00</p>
  <div class="brand-block">
    <div class="brand"><span class="brand-dot"></span><span class="brand-name">NEXO-VAULT</span></div>
    <div class="brand-url">www.nexo-vault.be</div>
  </div>
</section>

<section class="piece card-back">
  <p class="small">Rue des Vignots Hauts 42B · B-4280 CORNIVAL · Belgique<br>Gestion infrastructure informatique, serveurs, réseau<br>www.nexo-vault.be</p>
  <svg class="wave" viewBox="0 0 187 40" height="40" preserveAspectRatio="none" aria-hidden="true">
    <path d="M0 22 C60 30 120 6 187 14 L187 40 L0 40Z" fill="var(--grey)"/>
    <path d="M0 28 C60 36 120 12 187 20 L187 40 L0 40Z" fill="var(--red)"/>
  </svg>
</section>

<section class="piece letterhead">
  <div class="brand-block">
    <div class="brand"><span class="brand-dot"></span><span class="brand-name">NEXO-VAULT</span></div>
    <div class="brand-url">www.nexo-vault.be</div>
  </div>
  <p class="small contact">Nexo-Vault sprl<br>Rue des Vignots Hauts 42B<br>B-4280 CORNIVAL<br>T. +32 4 512 00 00<br>F. +32 4 512 00 01<br>mathis@nexo-vault.be</p>
  <div class="faint-mark" aria-hidden="true">NEXO-VAULT</div>
  <svg class="wave" viewBox="0 0 384 80" height="80" preserveAspectRatio="none" aria-hidden="true">
    <path d="M0 40 C110 62 250 20 384 36 L384 44 C250 28 110 70 0 50Z" fill="var(--grey)"/>
    <path d="M0 58 C120 76 260 34 384 48 L384 80 L0 80Z" fill="var(--red)"/>
  </svg>
</section>

<section class="piece envelope-back">
  <svg viewBox="0 0 492 218" preserveAspectRatio="none" aria-hidden="true">
    <defs>
      <linearGradient id="flap" x1="0" y1="0" x2="0" y2="1">
        <stop offset="0" stop-color="var(--red)"/>
        <stop offset="1" stop-color="var(--red-dark)"/>
      </linearGradient>
    </defs>
    <rect width="492" height="218" fill="url(#flap)"/>
    <path d="M0 110 C160 150 330 150 492 110 L492 218 L0 218Z" fill="var(--paper)"/>
  </svg>
</section>

<section class="piece envelope-front">
  <div class="brand-block">
    <div class="brand"><span class="brand-dot"></span><span class="brand-name">NEXO-VAULT</span></div>
    <div class="brand-url">www.nexo-vault.be</div>
  </div>
  <p class="small contact">Nexo-Vault sprl<br>Rue des Vignots Hauts 42B<br>B-4280 CORNIVAL<br>T. +32 4 512 00 00<br>mathis@nexo-vault.be</p>
  <svg class="wave" viewBox="0 0 492 70" height="70" preserveAspectRatio="none" aria-hidden="true">
    <path d="M0 30 C150 52 320 8 492 22 L492 30 C320 18 150 62 0 40Z" fill="var(--grey)"/>
    <path d="M0 46 C160 66 330 24 492 36 L492 70 L0 70Z" fill="var(--red)"/>
  </svg>
</section>

</body>
</html>
```